Events By Quellon

Weddings, Corporate, Special Events
Memorable Catering, Personalized Menus, Custom Layout & Designs
Professional Staff, Excellent Service
Our Mission is Turning YOUR Vision into a Reality

Dorrie Quellon, Principal Planner
ph. 202 555-0187 - fax 301-555-0142
Email - eventsbyquellon@mailhaven.net
Web - www.cateringbyquellon.net
cateringbyquellon@Instagram

Target Market(s)

All Brides, Corprate Business, Special Events

Industry/Entity Type

Hospitality

Contact Information for Business Card

clean but affective

Font styles to use
Serif
Sans Serif
Script

Colors

Designer to choose colors to be used in the design.

Requirements
Must have
• logo with tagline using colors that will enhance what
• some pictures of nice table scape, hors d'oevures, upscale foods......
Nice to have
• Event: Something that happens or is regarded as happening, an occurrence especially one of some importance.
Should not have
• Use Logo on both sides

```html
<!DOCTYPE html>
<html lang="en">
<head>
<meta charset="utf-8">
<title>Events By Quellon – Business Card</title>
<link rel="stylesheet" href="https://fonts.googleapis.com/css2?family=EB+Garamond:ital,wght@0,400;0,500;1,400&display=swap">
<style>
  :root {
    --cream: #fbf3ea;
    --blush: #f3dcd0;
    --rose-wash: #f1d3cc;
    --blue: #4a7fc2;
    --blue-soft: #5e93d3;
    --slate: #4d6883;
    --name-grey: #7a8796;
    --divider: #6f98cf;
  }
  * { margin: 0; padding: 0; box-sizing: border-box; }
  html, body { width: 1200px; height: 686px; overflow: hidden; background: var(--cream); }
  .card {
    position: relative;
    width: 1200px;
    height: 686px;
    overflow: hidden;
    font-family: "EB Garamond", Georgia, serif;
  }
  .backdrop {
    position: absolute; inset: 0;
    background: linear-gradient(180deg, #f7eadf 0%, #fbf2e9 55%, #fdf7f1 100%);
  }
  .floral {
    position: absolute; right: 0; top: 0;
    width: 560px; height: 686px;
    background: linear-gradient(200deg, var(--rose-wash) 0%, rgba(243,220,208,0.6) 45%, rgba(251,243,234,0) 85%);
  }
  .services, .mission {
    position: absolute;
    left: 47px; width: 600px;
    text-align: center;
    line-height: 46px;
    white-space: nowrap;
  }
  .services { top: 160px; color: var(--blue); font-size: 37px; }
  .services li { list-style: none; height: 46px; }
  .mission { top: 434px; color: var(--blue-soft); font-size: 38px; }
  .mission p { height: 46px; }
  .divider {
    position: absolute; left: 662px; top: 110px;
    width: 2px; height: 503px;
    background: var(--divider);
  }
  .contact {
    position: absolute; left: 711px; top: 0;
    line-height: 1;
    color: var(--slate);
    font-size: 35px;
  }
  .contact > * { position: absolute; left: 0; white-space: nowrap; }
  .contact .name { top: 136px; font-size: 44px; color: var(--name-grey); }
  .contact .title { top: 188px; font-size: 33px; font-style: italic; color: var(--blue); }
  .contact .phone { top: 278px; }
  .contact .fax { top: 326px; }
  .contact .email { top: 372px; }
  .contact .web { top: 463px; }
  .contact .social { top: 509px; display: flex; align-items: center; gap: 10px; }
  .social .mark { width: 26px; height: 26px; background: var(--blue-soft); display: inline-block; }
</style>
</head>
<body>
  <div class="card">
    <div class="backdrop" role="img" aria-label="Softly blurred photograph of an elegant wedding reception table setting in cream and blush tones"></div>
    <div class="floral" role="img" aria-label="Photograph of pale pink roses and greenery in a floral arrangement"></div>

    <ul class="services">
      <li>Weddings · Corporate · Special Events</li>
      <li>Memorable Catering · Personalized</li>
      <li>· Menus and Designs</li>
      <li>· Professional Staff</li>
    </ul>

    <div class="mission">
      <p>Our Mission is Turning YOUR Vision</p>
      <p>into a Reality</p>
    </div>

    <div class="divider"></div>

    <div class="contact">
      <p class="name">Dorrie Quellon</p>
      <p class="title">Principal Planner</p>
      <p class="phone">p:&nbsp; 202 555-0187</p>
      <p class="fax">f:&nbsp;&nbsp; 301-555-0142</p>
      <p class="email">e: eventsbyquellon@mailhaven.net</p>
      <p class="web">www.cateringbyquellon.net</p>
      <p class="social"><span class="mark"></span>cateringbyquellon</p>
    </div>
  </div>
</body>
</html>
```